Tri-fold flyer for Managed Services IT company

We need a tri-fold flyer design for our Managed Services IT company. Our website is here: https://pelicanfjordit.net. While we don't have to match our website we do want to incorporate the logo in the flyer. We would like a flyer that is *very* easy and quick to read/skim over and convey our message. Something like these:

https://www.artkestrel.com/design/58203917

https://47sketchyard.com/postcard-flyer-design/contests/create-lead-generating-flyer-postcard-managed-services-company-815243

http://www.marbleoaksystems.com/managed-services-no-cost-one-month/

Target Market(s)

Business to business IT services

Industry/Entity Type

It Service

Font styles to use
Serif
Sans Serif

Requirements
Must have
• *very* easy and quick to read/skim over and convey our message
Should not have
• verbose, lots of text

```html
<!DOCTYPE html>
<html lang="en">
<head>
<meta charset="utf-8">
<title>Pelican Fjord IT – Tri-fold Flyer</title>
<link rel="stylesheet" href="https://fonts.googleapis.com/css2?family=Open+Sans:wght@400;600;700;800&display=swap">
<style>
  :root {
    --navy: #0d2f6b;
    --blue: #17449a;
    --blue-deep: #0a2458;
    --orange: #e9781f;
    --orange-light: #f39a3a;
    --charcoal: #3a3d42;
    --white: #ffffff;
    --paper: #f4f5f7;
    --backdrop: #e3e4e6;
  }
  * { box-sizing: border-box; margin: 0; padding: 0; }
  html, body { width: 1200px; height: 800px; overflow: hidden; }
  body {
    background: var(--backdrop);
    font-family: "Open Sans", Arial, sans-serif;
    color: var(--white);
  }
  .flyer {
    position: absolute;
    left: 90px; top: 20px;
    width: 1020px; height: 760px;
    display: flex;
    box-shadow: 0 6px 24px rgba(0,0,0,.18);
  }
  .panel {
    position: relative;
    width: 340px; height: 760px;
    overflow: hidden;
  }
  .panel-shapes { position: absolute; inset: 0; width: 100%; height: 100%; }
  .photo { position: absolute; left: 0; width: 100%; }
  .web-address {
    position: absolute; left: 0; right: 0; bottom: 34px;
    text-align: center; font-size: 14px; font-weight: 400; color: var(--white);
  }
  .web-address strong { font-weight: 700; }
  .rule { width: 26px; height: 3px; background: var(--white); margin: 12px 0 16px; }

  /* About panel */
  .panel-about { background: linear-gradient(160deg, var(--navy) 0%, var(--blue-deep) 100%); }
  .panel-about .network {
    top: 300px; height: 360px;
    background: radial-gradient(ellipse at 40% 60%, rgba(70,140,230,.55) 0%, rgba(23,68,154,.35) 45%, rgba(10,36,88,0) 75%);
  }
  .about-copy { position: absolute; left: 34px; right: 28px; top: 62px; }
  .headline { font-size: 25px; font-weight: 800; line-height: 1.15; }
  .headline .accent { color: var(--orange); display: block; }
  .body-copy { font-size: 11.5px; line-height: 1.55; margin-bottom: 14px; }

  /* Contact panel */
  .panel-contact { background: var(--blue); }
  .panel-contact .team-photo {
    top: 0; height: 330px;
    background: linear-gradient(180deg, #eef1f4 0%, #cfd8e2 60%, #9aa9bb 100%);
  }
  .contact-copy { position: absolute; left: 0; right: 0; top: 395px; text-align: center; }
  .contact-copy .rule { margin: 10px auto 18px; }
  .section-title { font-size: 24px; font-weight: 700; }
  .office { font-size: 12.5px; line-height: 1.45; margin-bottom: 10px; color: #dbe4f5; }
  .office strong { display: block; font-size: 13.5px; color: var(--white); }
  .phone {
    display: inline-flex; align-items: center; gap: 10px;
    font-size: 26px; font-weight: 700; margin-top: 10px;
  }

  /* Cover panel */
  .panel-cover { background: var(--paper); }
  .brand {
    position: absolute; top: 58px; left: 0; right: 0;
    display: flex; justify-content: center; align-items: center; gap: 10px;
    font-size: 23px; font-weight: 700; letter-spacing: 2px; color: var(--navy);
  }
  .brand-dot { width: 14px; height: 14px; border-radius: 50%; background: var(--orange); }
  .panel-cover .keyboard-photo {
    top: 120px; height: 320px;
    background: linear-gradient(170deg, #f1f2f4 0%, #d9dde3 45%, #8e96a3 100%);
  }
  .cover-copy { position: absolute; left: 38px; right: 30px; top: 458px; }
  .cover-copy .section-title { font-size: 23px; line-height: 1.2; }
  .tagline { font-size: 12.5px; line-height: 1.5; color: #dbe4f5; }
</style>
</head>
<body>
<main class="flyer">

  <section class="panel panel-about">
    <div class="photo network" role="img" aria-label="Abstract blue digital network of connected lines and glowing dots"></div>
    <div class="about-copy">
      <h1 class="headline">The DC Metro <span class="accent">IT Support Experts</span></h1>
      <div class="rule"></div>
      <p class="body-copy">Pelican Fjord IT has been serving the Bethesda area since 2005, providing IT Support such as technical helpdesk support, computer support, and consulting to small and medium-sized businesses. It's always been our goal to provide enterprise-level IT practices and solutions to the small business sector, with small business prices. Our experience has allowed us to build and develop the infrastructure needed to keep our prices affordable and our clients up and running.</p>
      <p class="body-copy">We partner with many types of businesses in the area, and strive to eliminate IT issues before they cause expensive downtime, so you can continue to drive your business forward. Our dedicated staff loves seeing our clients succeed. Your success is our success, and as you grow, we grow.</p>
    </div>
    <svg class="panel-shapes" viewBox="0 0 340 760" preserveAspectRatio="none" aria-hidden="true">
      <path d="M0 700 C120 690 240 670 340 640 L340 760 L0 760 Z" fill="var(--orange)"/>
    </svg>
    <p class="web-address">www.<strong>PelicanFjordIT</strong>.net</p>
  </section>

  <section class="panel panel-contact">
    <div class="photo team-photo" role="img" aria-label="Photo of three colleagues working together at an office table"></div>
    <svg class="panel-shapes" viewBox="0 0 340 760" preserveAspectRatio="none" aria-hidden="true">
      <path d="M0 300 C110 320 230 320 340 290 L340 760 L0 760 Z" fill="var(--charcoal)"/>
      <path d="M0 322 C110 345 230 345 340 315 L340 760 L0 760 Z" fill="var(--blue)"/>
      <path d="M0 700 C120 690 240 670 340 645 L340 760 L0 760 Z" fill="var(--orange)"/>
    </svg>
    <div class="contact-copy">
      <h2 class="section-title">Contact Us</h2>
      <div class="rule"></div>
      <p class="office"><strong>Pelican Fjord IT</strong>418 Harbor Crest Lane 2B<br>Fairhaven, Maryland 20899</p>
      <p class="office"><strong>Pelican Fjord IT</strong>2270 Lantern Hill Ave, Suite 300<br>Washington, DC 20099</p>
      <p class="phone">
        <svg width="22" height="22" viewBox="0 0 24 24" aria-hidden="true">
          <circle cx="12" cy="12" r="10.5" fill="none" stroke="var(--orange)" stroke-width="2"/>
          <path d="M8.2 6.8l1.8-.4 1.1 2.6-1.2.9c.6 1.4 1.6 2.4 3 3l.9-1.2 2.6 1.1-.4 1.8c-4.2.3-8.1-3.6-7.8-7.8z" fill="var(--orange)"/>
        </svg>
        301-555-0148
      </p>
    </div>
    <p class="web-address">www.<strong>PelicanFjordIT</strong>.net</p>
  </section>

  <section class="panel panel-cover">
    <div class="brand"><span class="brand-dot"></span>PELICAN FJORD IT</div>
    <div class="photo keyboard-photo" role="img" aria-label="Close-up photo of hands typing on a laptop keyboard with network icons overlaid"></div>
    <svg class="panel-shapes" viewBox="0 0 340 760" preserveAspectRatio="none" aria-hidden="true">
      <path d="M0 420 C120 415 240 390 340 330 L340 760 L0 760 Z" fill="var(--orange)"/>
      <path d="M0 425 C130 425 250 415 340 385 L340 760 L0 760 Z" fill="var(--charcoal)"/>
      <path d="M0 438 C130 438 250 428 340 400 L340 760 L0 760 Z" fill="var(--blue)"/>
      <path d="M0 700 C120 690 240 670 340 645 L340 760 L0 760 Z" fill="var(--orange)"/>
    </svg>
    <div class="cover-copy">
      <h2 class="section-title">IT Solutions<br>Designed For You</h2>
      <div class="rule"></div>
      <p class="tagline">eliminate downtime, improve collaboration, and focus on your business instead of your IT</p>
    </div>
    <p class="web-address">www.<strong>PelicanFjordIT</strong>.net</p>
  </section>

</main>
</body>
</html>
```